Ridgeway Hearth Partners Business Card

Looking for a new business card layout. We are a real estate firm w/ a logo, old design attached. Must keep the same elements on there, just need a fresh look and possible some foil accents. Looking for a simpler design w/ more modern style.

Target Market(s)

Real Estate clients

Industry/Entity Type

Real Estate Agent

Contact Information for Business Card

Font styles to use
Sans Serif

Requirements
Must have
• all elements on current biz card
Nice to have
• modern look, simpler than we have!
Should not have
• no serif fonts

```html
<!DOCTYPE html>
<html lang="en">
<head>
<meta charset="utf-8">
<title>Ridgeway Hearth Partners Business Card</title>
<link href="https://fonts.googleapis.com/css2?family=Montserrat:wght@400;500;700&display=swap" rel="stylesheet">
<style>
  :root {
    --teal: #36bccb;
    --teal-deep: #1f9aa8;
    --white: #ffffff;
    --arc-grey: #9a9a9a;
    --stage: #2b2b2d;
  }
  * { margin: 0; padding: 0; box-sizing: border-box; }
  html, body { width: 1200px; height: 900px; overflow: hidden; }
  body {
    background: var(--stage);
    font-family: "Montserrat", sans-serif;
    position: relative;
  }
  .card {
    position: absolute;
    left: 250px;
    width: 700px;
    height: 400px;
    border-radius: 18px;
    overflow: hidden;
    background: var(--teal);
  }
  .card-back { top: 35px; display: flex; align-items: center; justify-content: center; }
  .card-front { top: 465px; }
  .brand-name {
    color: var(--teal-deep);
    font-weight: 700;
    font-size: 38px;
    letter-spacing: 2px;
    text-transform: uppercase;
  }
  .front-shape { position: absolute; inset: 0; }
  .front-brand {
    position: absolute;
    left: 390px;
    top: 178px;
    width: 300px;
    text-align: center;
    color: var(--teal);
    font-weight: 700;
    font-size: 24px;
    line-height: 1.25;
    letter-spacing: 1.5px;
    text-transform: uppercase;
  }
  .contact {
    position: absolute;
    left: 60px;
    top: 68px;
    color: var(--white);
  }
  .contact-name {
    font-weight: 700;
    font-size: 28px;
    letter-spacing: 3px;
    text-transform: uppercase;
  }
  .contact-title { font-size: 15px; font-weight: 500; margin-top: 2px; }
  .contact-address { font-size: 15px; line-height: 1.35; margin-top: 12px; }
  .contact-list { list-style: none; margin-top: 12px; font-size: 15.5px; }
  .contact-list li { display: flex; align-items: center; gap: 10px; line-height: 1.65; }
  .contact-list svg { width: 14px; height: 14px; flex: none; }
</style>
</head>
<body>
  <section class="card card-back">
    <p class="brand-name">Ridgeway Hearth Partners</p>
  </section>

  <section class="card card-front">
    <svg class="front-shape" viewBox="0 0 700 400" width="700" height="400">
      <circle cx="560" cy="200" r="235" fill="var(--arc-grey)"/>
      <circle cx="572" cy="200" r="232" fill="var(--white)"/>
    </svg>
    <p class="front-brand">Ridgeway Hearth<br>Partners</p>

    <div class="contact">
      <h1 class="contact-name">Marla Quinn</h1>
      <p class="contact-title">Principal Broker</p>
      <p class="contact-address">218 NE Birch Ln Larkfield,<br>OR 97310</p>
      <ul class="contact-list">
        <li>
          <svg viewBox="0 0 24 24" fill="none" stroke="#fff" stroke-width="2"><path d="M5 3h4l2 5-3 2a12 12 0 0 0 6 6l2-3 5 2v4a2 2 0 0 1-2 2A17 17 0 0 1 3 5a2 2 0 0 1 2-2z"/></svg>
          555.204.3310
        </li>
        <li>
          <svg viewBox="0 0 24 24" fill="none" stroke="#fff" stroke-width="2"><rect x="6" y="2" width="12" height="20" rx="2"/><line x1="11" y1="18" x2="13" y2="18"/></svg>
          555.318.6042
        </li>
        <li>
          <svg viewBox="0 0 24 24" fill="none" stroke="#fff" stroke-width="2"><rect x="3" y="5" width="18" height="14" rx="1"/><path d="M3 6l9 7 9-7"/></svg>
          marla@ridgewayhearth.com
        </li>
        <li>
          <svg viewBox="0 0 24 24" fill="none" stroke="#fff" stroke-width="2"><circle cx="12" cy="12" r="9"/><path d="M3 12h18M12 3c3 3 3 15 0 18M12 3c-3 3-3 15 0 18"/></svg>
          RidgewayHearth-Homes.com
        </li>
      </ul>
    </div>
  </section>
</body>
</html>
```